Marlow Bridge needs a brochure review

We are a company operating in more than 10 countries that, since 1972, has the ambitious and innovative objective to stimulate foreign language learning by discovering different countries and cultures, through training courses tailored to individual needs
We need a layout review of our brochure in order to make the content clearer, immediate and appealing and, at the same time, make the layout more modern and young.
The pages we need are: the cover and pages 3, 5, 7, 20, 21, 22, 23, 34, 36, 37. You will find our actual brochure pdf as attachment

Target Market(s)

Students and families, business

Industry/Entity Type

It Company

Requirements
Must have
• The same written information as the actual one.
• Blue and green colours.
• The cover must be simple, elegant and clean but new and effective. In addition to the cover the pages you should review are number :2, 3, 4, 5, 6, 7. Feel free to use new background, images and new layout for the text.

```html
<!DOCTYPE html>
<html lang="it">
<head>
<meta charset="utf-8">
<title>Marlow Bridge – Vacanze Studio 2017</title>
<link rel="stylesheet" href="https://fonts.googleapis.com/css2?family=Roboto:wght@400;500;700&family=Roboto+Condensed:wght@400;700&display=swap">
<style>
  :root {
    --page-bg: #efefef;
    --card-bg: #f7f7f7;
    --dark: #2e2e2e;
    --blue: #2f7fd6;
    --green: #5aa81c;
    --text-grey: #3a3a3a;
    --text-dark: #222222;
    --white: #ffffff;
  }
  html, body {
    margin: 0;
    padding: 0;
    width: 1200px;
    height: 1200px;
    overflow: hidden;
    background: var(--page-bg);
  }
  .canvas {
    position: relative;
    width: 1200px;
    height: 1200px;
  }
  .card {
    position: absolute;
    top: 237px;
    width: 513px;
    height: 663px;
    background: var(--card-bg);
    box-shadow: 0 4px 14px rgba(0,0,0,0.12);
  }
  .card--front { left: 53px; }
  .card--back { left: 644px; }
  .card svg { display: block; width: 100%; height: 100%; }
  .sans { font-family: "Roboto", sans-serif; }
  .condensed { font-family: "Roboto Condensed", sans-serif; }
</style>
</head>
<body>
<div class="canvas">

  <section class="card card--front">
    <svg viewBox="0 0 598 773" xmlns="http://www.w3.org/2000/svg">
      <defs>
        <linearGradient id="front-dark" x1="0" y1="0" x2="1" y2="0">
          <stop offset="0" stop-color="#2a2a2a"/>
          <stop offset="1" stop-color="#5a5a5a"/>
        </linearGradient>
        <linearGradient id="front-photo" x1="0" y1="0" x2="1" y2="1">
          <stop offset="0" stop-color="#d98a6a"/>
          <stop offset="0.45" stop-color="#f0c7c0"/>
          <stop offset="1" stop-color="#c9866c"/>
        </linearGradient>
        <linearGradient id="white-area" x1="0" y1="0" x2="0" y2="1">
          <stop offset="0" stop-color="#e8e8e8"/>
          <stop offset="1" stop-color="#ffffff"/>
        </linearGradient>
      </defs>

      <rect class="card-base" width="598" height="773" fill="url(#white-area)"/>

      <path class="dark-band" fill="url(#front-dark)"
        d="M0,335 C40,380 100,420 180,440 C320,470 500,420 598,310 V410 C560,450 480,490 380,520 C250,560 120,640 0,745 Z"/>

      <path class="blue-swoosh-lower" fill="none" stroke="var(--blue)" stroke-width="10"
        d="M0,745 C120,640 250,560 380,520 C480,490 560,450 598,410"/>
      <path class="blue-swoosh-upper" fill="none" stroke="var(--blue)" stroke-width="26"
        d="M0,348 C40,393 100,433 180,453 C320,483 500,433 598,323"/>

      <g role="img" aria-label="Foto di due ragazze sorridenti con cappello e occhiali da sole in città">
        <path class="hero-photo" fill="url(#front-photo)"
          d="M0,0 H598 V310 C500,420 320,470 180,440 C100,420 40,380 0,335 Z"/>
      </g>

      <text class="brand-name sans" x="45" y="548" font-weight="700" font-size="31" fill="var(--white)">Marlow Bridge</text>

      <text x="556" y="582" text-anchor="end" class="sans" font-weight="500" font-size="37" fill="var(--text-grey)">Vacanze</text>
      <text x="556" y="624" text-anchor="end" class="sans" font-weight="500" font-size="44" fill="var(--green)">Studio 2017</text>
      <text x="550" y="649" text-anchor="end" class="condensed" font-size="14" fill="var(--text-grey)">DAI 10 AI 18 ANNI DI</text>
      <text x="550" y="666" text-anchor="end" class="condensed" font-size="14" fill="var(--text-grey)">GRUPPO CON ACCOMPAGNATORE</text>
      <text x="556" y="723" text-anchor="end" class="sans" font-size="51" fill="var(--green)">L'estate che sogni</text>
      <text x="556" y="758" text-anchor="end" class="sans" font-size="13" letter-spacing="3.5" fill="var(--text-grey)">www.marlowbridge.it</text>
    </svg>
  </section>

  <section class="card card--back">
    <svg viewBox="0 0 598 773" xmlns="http://www.w3.org/2000/svg">
      <defs>
        <linearGradient id="back-photo" x1="0" y1="0" x2="0" y2="1">
          <stop offset="0" stop-color="#c4c4c4"/>
          <stop offset="0.6" stop-color="#dedede"/>
          <stop offset="1" stop-color="#f7f7f7"/>
        </linearGradient>
        <linearGradient id="back-dark" x1="0" y1="0" x2="1" y2="0">
          <stop offset="0" stop-color="#2c2c2c"/>
          <stop offset="1" stop-color="#484848"/>
        </linearGradient>
      </defs>

      <rect class="card-base" width="598" height="773" fill="var(--card-bg)"/>

      <g role="img" aria-label="Foto sbiadita in bianco e nero di un gruppo di ragazzi sorridenti abbracciati">
        <rect class="group-photo" x="0" y="0" width="598" height="440" fill="url(#back-photo)"/>
      </g>

      <text x="299" y="387" text-anchor="middle" class="sans" font-weight="500" font-size="15" fill="var(--blue)">PER INFORMAZIONI E PRENOTAZIONI:</text>

      <g class="office office--milano sans" font-size="15" fill="var(--text-dark)">
        <text x="45" y="436" font-weight="500" fill="var(--blue)">Milano</text>
        <path d="M47,448 h3 l1,3 -1.5,1 q1,2 3,3 l1,-1.5 3,1 v3 q-7,0 -9.5,-9.5z" fill="var(--green)"/>
        <text x="57" y="458">+39 02 40218810</text>
        <rect x="46" y="470" width="9" height="6" rx="1.5" fill="var(--green)"/>
        <text x="61" y="477">+39 02 402188122</text>
        <path d="M50,485 a4,4 0 0 1 4,4 c0,3 -4,8 -4,8 c0,0 -4,-5 -4,-8 a4,4 0 0 1 4,-4 z" fill="var(--green)"/>
        <circle cx="50" cy="489" r="1.5" fill="var(--card-bg)"/>
        <text x="57" y="496">20121 - Via dei Tigli, 14</text>
      </g>

      <g class="office office--roma sans" font-size="15" fill="var(--text-dark)">
        <text x="338" y="436" font-weight="500" fill="var(--blue)">Roma</text>
        <path d="M340,448 h3 l1,3 -1.5,1 q1,2 3,3 l1,-1.5 3,1 v3 q-7,0 -9.5,-9.5z" fill="var(--green)"/>
        <text x="356" y="458">+39 06 51290733</text>
        <rect x="339" y="470" width="9" height="6" rx="1.5" fill="var(--green)"/>
        <text x="356" y="477">+39 06 51290745</text>
        <path d="M343,485 a4,4 0 0 1 4,4 c0,3 -4,8 -4,8 c0,0 -4,-5 -4,-8 a4,4 0 0 1 4,-4 z" fill="var(--green)"/>
        <circle cx="343" cy="489" r="1.5" fill="var(--card-bg)"/>
        <text x="356" y="496">00153 - Via delle Rose 9</text>
      </g>

      <path class="footer-shade" fill="#dcdcdc"
        d="M0,677 C120,572 250,527 350,530 C450,533 540,602 598,702 V773 H0 Z"/>
      <path class="footer-band" fill="url(#back-dark)"
        d="M0,695 C120,590 250,545 350,548 C450,551 540,620 598,720 V773 H0 Z"/>
      <path class="footer-blue" fill="none" stroke="var(--blue)" stroke-width="16"
        d="M0,695 C120,590 250,545 350,548 C450,551 540,620 598,720"/>

      <text class="brand-name sans" x="299" y="667" text-anchor="middle" font-weight="700" font-size="31" fill="var(--white)">Marlow Bridge</text>

      <g class="contact sans" font-size="20" font-weight="500" fill="var(--white)">
        <rect x="190" y="722" width="14" height="10" fill="var(--white)"/>
        <path d="M190,722 L197,728 L204,722" fill="none" stroke="#333" stroke-width="1.5"/>
        <text x="213" y="733">info@marlowbridge.it</text>
        <circle cx="197" cy="752" r="7" fill="none" stroke="var(--white)" stroke-width="1.6"/>
        <path d="M190,752 H204 M197,745 C193,749 193,755 197,759 M197,745 C201,749 201,755 197,759" fill="none" stroke="var(--white)" stroke-width="1.2"/>
        <text x="213" y="758">www.marlowbridge.it</text>
      </g>
    </svg>
  </section>

</div>
</body>
</html>
```